Luxury Business Card Design for High-End Window Treatments

Gilded Vantages
Custom Plantation Shutters & Architectural Shading Systems

⸻

BACK

Daniel Forsythe
Owner

Custom Interior & Exterior Window Treatments

919-482-7034
gildedvantages.com

I have included a picture that I’m hoping we can use on the back, but I’m also wondering if you can get rid of the ladder? Should we get rid of shutters , shades and blinds underneath Gilded Vantages?

Target Market(s)

High-end residential homeowners, custom home builders, architects, interior designers, and luxury renovation clients seeking premium plantation shutters and motorized architectural shading systems.

Industry/Entity Type

Custom Window treatments

Contact Information for Business Card

Front Gilded Vantages Custom Plantation Shutters Motorized Architectural Shading Systems BACK Daniel Forsythe Owner 919-482-7034 GildedVantages.com Custom Interior & Exterior Window Treatments By Appointment

Requirements
Nice to have
• Not 100% sure on nice to halves or the color but you can definitely check out my website to get a better understanding of what I’m trying to do

```html
<!DOCTYPE html>
<html lang="en">
<head>
<meta charset="utf-8">
<title>Gilded Vantages – Business Card</title>
<link rel="stylesheet" href="https://fonts.googleapis.com/css2?family=Playfair+Display:wght@400;700&family=Montserrat:wght@400;500&display=swap">
<style>
  :root {
    --page: #e7e2d8;
    --card-black: #050505;
    --card-black-soft: #1b1b1b;
    --gold: #c9b56e;
    --gold-deep: #a8944f;
    --gold-light: #ddd0a0;
    --ivory: #f1ece0;
    --white: #f5f5f5;
  }
  * { box-sizing: border-box; margin: 0; padding: 0; }
  html, body { width: 916px; height: 1200px; overflow: hidden; }
  body {
    background: var(--page);
    font-family: "Montserrat", Arial, sans-serif;
    position: relative;
  }
  .card {
    position: absolute;
    left: 72px;
    width: 773px;
    height: 460px;
    border-radius: 24px;
    overflow: hidden;
    box-shadow: 0 10px 24px rgba(0,0,0,0.35);
  }
  .card--front {
    top: 107px;
    background: linear-gradient(100deg, var(--card-black-soft) 0%, var(--card-black) 35%, var(--card-black) 100%);
  }
  .card--back {
    top: 640px;
    background: #0c0c0c;
  }
  .wave { position: absolute; inset: 0; width: 100%; height: 100%; }

  .brand { position: absolute; text-align: center; }
  .brand__name {
    font-family: "Playfair Display", Georgia, serif;
    font-weight: 400;
    line-height: 1.05;
  }
  .brand__tagline {
    font-family: "Playfair Display", Georgia, serif;
    color: var(--gold);
    word-spacing: 0.5em;
  }
  .card--front .brand { left: 90px; top: 158px; width: 270px; }
  .card--front .brand__name { font-size: 42px; color: var(--gold); }
  .card--front .brand__tagline { font-size: 18px; margin-top: 10px; }

  .divider {
    position: absolute;
    left: 395px; top: 128px;
    width: 2px; height: 200px;
    background: var(--gold);
  }
  .contact { position: absolute; left: 421px; top: 122px; color: var(--white); }
  .contact__name {
    font-family: "Playfair Display", Georgia, serif;
    font-weight: 700;
    font-size: 28px;
    color: var(--gold);
    letter-spacing: 0.3px;
  }
  .contact__role { font-size: 16px; margin-top: 2px; }
  .contact__service { font-size: 16.5px; line-height: 1.4; margin-top: 12px; }
  .contact__line { display: flex; align-items: center; gap: 10px; font-size: 17px; margin-top: 6px; }
  .contact__line:first-of-type { margin-top: 14px; }
  .contact__icon { width: 17px; height: 17px; fill: var(--white); flex: none; }
  .contact__note { font-size: 16.5px; color: var(--gold); margin-top: 14px; }

  .back-photo {
    position: absolute; inset: 0;
    background:
      radial-gradient(ellipse at 70% 40%, rgba(70,66,58,0.55), transparent 65%),
      linear-gradient(180deg, #161616 0%, #232220 45%, #111 100%);
  }
  .card--back .brand { left: 0; right: 0; top: 108px; }
  .card--back .brand__name { font-size: 80px; color: var(--ivory); }
  .card--back .brand__tagline { font-size: 30px; margin-top: 12px; color: var(--gold-light); }
</style>
</head>
<body>

  <section class="card card--front" aria-label="Card front">
    <svg class="wave" viewBox="0 0 773 460" preserveAspectRatio="none" aria-hidden="true">
      <defs>
        <linearGradient id="goldSweep" x1="0" y1="0" x2="1" y2="0">
          <stop offset="0" stop-color="var(--gold-light)"/>
          <stop offset="0.5" stop-color="var(--gold)"/>
          <stop offset="1" stop-color="var(--gold-deep)"/>
        </linearGradient>
      </defs>
      <path d="M0,385 C120,345 260,350 400,385 C540,420 660,410 773,352 L773,460 L0,460 Z" fill="url(#goldSweep)"/>
      <path d="M200,350 C340,352 470,420 590,428 C670,433 730,410 773,392" fill="none" stroke="var(--card-black)" stroke-width="9"/>
    </svg>

    <div class="brand">
      <p class="brand__name">Gilded<br>Vantages</p>
      <p class="brand__tagline">Shutters Shades Blinds</p>
    </div>

    <div class="divider"></div>

    <div class="contact">
      <p class="contact__name">Daniel Forsythe</p>
      <p class="contact__role">Owner</p>
      <p class="contact__service">Custom Interior &amp; Exterior<br>Window Treatments</p>
      <p class="contact__line">
        <svg class="contact__icon" viewBox="0 0 20 20" aria-hidden="true"><path d="M2 6c0-2 3-3 8-3s8 1 8 3v2h-4V6.5c-1-.5-2.5-.7-4-.7s-3 .2-4 .7V8H2z"/><path d="M5 9h10l2 8H3z"/><circle cx="10" cy="13" r="2" fill="#050505"/></svg>
        919-482-7034
      </p>
      <p class="contact__line">
        <svg class="contact__icon" viewBox="0 0 20 20" aria-hidden="true"><circle cx="10" cy="10" r="8"/><path d="M6 6c2 0 3 1 2 3s1 3 0 5M13 4c-1 2 1 3 3 3M12 16c0-2 2-3 4-2" stroke="#050505" stroke-width="1.4" fill="none"/></svg>
        GildedVantages.com
      </p>
      <p class="contact__note">By Appointment</p>
    </div>
  </section>

  <section class="card card--back" aria-label="Card back">
    <div class="back-photo" role="img" aria-label="Darkened photograph of a home porch with large shuttered windows"></div>
    <div class="brand">
      <p class="brand__name">Gilded<br>Vantages</p>
      <p class="brand__tagline">Shutters Shades Blinds</p>
    </div>
  </section>

</body>
</html>
```